Design for Perch Lane real estate agency

Incorporate logo into new business cards. I need to include the Marlowe Ridge logo incorporated into Perch Lane on one side of the card (attached). On the other side I see just the icon with "Tessa Lorne" (attached) with "Rooted in Care" either included as is or removed from logo and rather put as a tag line on the business card separate from the main logo. Contact information:

Tessa Lorne
Associate Broker
Cell: 914-555-0173
Email: tessalorne@perchlane.example
Web: www.perchlane.example

Target Market(s)

Buyers, Sellers, Builders and Investors of homes and land

Industry/Entity Type

Real Estate Agent

Contact Information for Business Card

My client base tend to be higher end home buyers, sellers, builders and investors. I have been more and more in land and subdivisions for builders and investors. The card should not be cluttered. Clean and simple - yet with an air of exclusive/high end

Colors

Designer to choose colors to be used in the design.

Requirements
Must have
• Must have the logo on one side that has Marlowe Ridge logo incorporated. The side that has my contact information does not have to have the Marlowe Ridge logo incorporated.
• Must include "Rooted in Care" tag line either within logo (as is) or removed from logo and included in another position on the side of the business card with contact information.
Should not have
• Should not have Marlowe Ridge logo incorporated into Perch Lane logo on both sides of business card. Would like the Perch Lane logo that has Marlowe Logo only on the back side of card without contact information.

```html
<!DOCTYPE html>
<html lang="en">
<head>
<meta charset="utf-8">
<title>Perch Lane — Tessa Lorne Business Card</title>
<link rel="stylesheet" href="https://fonts.googleapis.com/css2?family=Cinzel:wght@400;600&family=Open+Sans:wght@400;600&display=swap">
<style>
  :root {
    --backdrop: #3b3430;
    --card: #0d0d0d;
    --card-edge: #1a1a1a;
    --gold: #d8a826;
    --gold-deep: #8a6a1c;
    --grey: #9a9a9a;
    --white: #ececec;
    --rule: #3a3a3a;
  }
  * { margin: 0; padding: 0; box-sizing: border-box; }
  html, body {
    width: 1200px; height: 900px; overflow: hidden;
    background: var(--backdrop);
  }
  .canvas {
    position: relative; width: 1200px; height: 900px;
    display: flex; align-items: center; justify-content: center; gap: 50px;
  }
  .card {
    position: relative; width: 525px; height: 300px;
    background: var(--card);
    border: 1px solid var(--card-edge);
    box-shadow: 0 14px 30px rgba(0,0,0,.45);
  }

  /* Contact side */
  .card-front { display: flex; }
  .identity {
    width: 235px; display: flex; flex-direction: column;
    align-items: center; justify-content: center; gap: 6px;
  }
  .identity-mark {
    display: flex; align-items: center; gap: 10px;
  }
  .identity-dot {
    width: 14px; height: 14px; border-radius: 50%; background: var(--gold);
  }
  .identity-name {
    font-family: 'Cinzel', serif; font-weight: 600;
    font-size: 26px; letter-spacing: 4px; color: var(--gold-deep);
  }
  .identity-tagline {
    font-family: 'Open Sans', sans-serif; font-weight: 400;
    font-size: 15px; letter-spacing: 1.5px; color: var(--grey);
    text-transform: uppercase;
  }
  .divider {
    width: 1px; margin: 40px 0; background: var(--rule);
  }
  .contact {
    padding: 48px 0 0 26px; display: flex; flex-direction: column;
  }
  .contact-name {
    font-family: 'Cinzel', serif; font-weight: 600;
    font-size: 19px; letter-spacing: 1px; color: var(--gold);
  }
  .contact-title {
    font-family: 'Open Sans', sans-serif; font-size: 11px;
    letter-spacing: .5px; color: var(--gold-deep); text-transform: uppercase;
    margin-bottom: 20px;
  }
  .contact-list { list-style: none; display: flex; flex-direction: column; gap: 4px; }
  .contact-item {
    display: flex; align-items: center; gap: 8px;
    font-family: 'Open Sans', sans-serif; font-size: 12px; color: var(--gold-deep);
  }
  .contact-item svg { width: 11px; height: 11px; flex: none; }

  /* Brand side */
  .card-back {
    display: flex; flex-direction: column; align-items: center; justify-content: center;
  }
  .brand-row { display: flex; align-items: center; gap: 14px; }
  .brand-dot { width: 18px; height: 18px; border-radius: 50%; background: var(--white); }
  .brand-name {
    font-family: 'Cinzel', serif; font-weight: 400;
    font-size: 36px; color: var(--white);
  }
  .brand-rule { width: 300px; height: 1px; background: var(--grey); margin: 6px 0 4px; }
  .brand-agent {
    font-family: 'Cinzel', serif; font-size: 14px; letter-spacing: 5px; color: var(--white);
  }
  .brand-tagline {
    font-family: 'Open Sans', sans-serif; font-size: 9px; letter-spacing: 3px;
    color: var(--grey); text-transform: uppercase;
  }
  .partner {
    display: flex; align-items: center; gap: 8px; margin-top: 18px;
  }
  .partner-square { width: 10px; height: 10px; background: var(--grey); }
  .partner-name {
    font-family: 'Open Sans', sans-serif; font-weight: 600;
    font-size: 11px; letter-spacing: 1px; color: var(--grey); text-transform: uppercase;
  }
</style>
</head>
<body>
<main class="canvas">
  <section class="card card-front" aria-label="Contact side">
    <div class="identity">
      <div class="identity-mark">
        <span class="identity-dot"></span>
        <span class="identity-name">TESSA LORNE</span>
      </div>
      <span class="identity-tagline">Rooted in Care</span>
    </div>
    <div class="divider"></div>
    <div class="contact">
      <h1 class="contact-name">TESSA LORNE</h1>
      <p class="contact-title">Associate Broker</p>
      <ul class="contact-list">
        <li class="contact-item">
          <svg viewBox="0 0 12 12"><path d="M2.5 1 L4.5 1 L5.2 3.5 L4 4.6 Q5.2 7 7.4 8 L8.5 6.8 L11 7.5 L11 9.5 Q10.5 11 9 11 Q1 10 1 2.5 Q1 1 2.5 1Z" fill="var(--gold)"/></svg>
          914-555-0173
        </li>
        <li class="contact-item">
          <svg viewBox="0 0 12 12"><rect x="1" y="2.5" width="10" height="7" fill="var(--gold)"/><path d="M1 2.5 L6 6.5 L11 2.5" stroke="var(--card)" stroke-width="1" fill="none"/></svg>
          tessalorne@perchlane.example
        </li>
        <li class="contact-item">
          <svg viewBox="0 0 12 12"><circle cx="6" cy="6" r="5" fill="var(--gold)"/><path d="M1 6 H11 M6 1 Q3 6 6 11 M6 1 Q9 6 6 11" stroke="var(--card)" stroke-width=".8" fill="none"/></svg>
          www.perchlane.example
        </li>
      </ul>
    </div>
  </section>

  <section class="card card-back" aria-label="Brand side">
    <div class="brand-row">
      <span class="brand-dot"></span>
      <span class="brand-name">Perch Lane</span>
    </div>
    <div class="brand-rule"></div>
    <span class="brand-agent">TESSA LORNE</span>
    <span class="brand-tagline">Rooted in Care</span>
    <div class="partner">
      <span class="partner-square"></span>
      <span class="partner-name">Marlowe Ridge</span>
    </div>
  </section>
</main>
</body>
</html>
```